A5 8pp Brochure - all copy, images, rough layout supplied

A5 8pp Brochure (front/back cover and 6pp inside).
All copy and images supplied. Layout and image placement suggestions provided.

The focus for this brochure is about making custom made uniforms for dance studios. This brochure will be given to dance school owners.

They want to communicate the process and also the fact that dance schools can make money from on-selling the uniforms to their students, so an additional income stream for the school.

Simple colour palette mainly black, grey, white and purple. I imagine the images supplied will provide most of the colour/pop for the brochure. Please look at the website for basic look and feel. I have also attached a mocked up flyer to show you a style that we like.

All referenced files and images should be attached.

Just need someone to put it together beautifully for me.

Reason: Extending deadline for 2 days. All submissions needed by end of day Tuesday 1 Sept. Thank you.

Target Market(s)

Dance studio owners / teachers

Font styles to use
Serif
Sans Serif

Colors
876aae
886aae
b7a5cd
e4daeb
f3f1f8
000000
ffffff
848484

Requirements
Must have
• Images of the custom made uniforms

```html
<!DOCTYPE html>
<html lang="en">
<head>
<meta charset="UTF-8">
<title>Our Development Procedure</title>
<link href="https://fonts.googleapis.com/css2?family=Arimo:wght@400;700&display=swap" rel="stylesheet">
<style>
  :root {
    --purple: #876aae;
    --purple-deep: #6f4f9c;
    --lilac: #b7a5cd;
    --lavender: #e4daeb;
    --mist: #f3f1f8;
    --ink: #000000;
    --paper: #ffffff;
    --grey: #848484;
    --band: #d2d2d2;
    --band-light: #e4e4e4;
  }
  * { margin: 0; padding: 0; box-sizing: border-box; }
  html, body { width: 847px; height: 1200px; overflow: hidden; background: var(--paper); }
  body { font-family: "Arimo", Arial, sans-serif; color: var(--grey); }
  .page { position: relative; width: 847px; height: 1200px; overflow: hidden; }

  .header-accent {
    position: absolute; top: 0; right: 0; width: 430px; height: 88px;
    border-bottom-left-radius: 100% 100%;
    background: linear-gradient(100deg, var(--lavender) 0%, var(--lilac) 45%, var(--purple) 100%);
  }

  .footer-band {
    position: absolute; left: 0; right: 0; top: 1082px; bottom: 0;
    background: var(--band);
  }
  .footer-band::after {
    content: ""; position: absolute; left: 0; right: 0; bottom: 0; height: 46px;
    background: var(--band-light);
  }

  .block { position: absolute; left: 135px; width: 577px; }
  .page-title { top: 118px; font-size: 36px; font-weight: 700; color: var(--ink); line-height: 44px; }
  .section-title { font-size: 25px; font-weight: 700; color: var(--purple); line-height: 30px; }
  .design-title { top: 190px; }
  .design-copy { top: 238px; }
  .sampling-title { top: 446px; }
  .sampling-copy { top: 505px; }
  .timing { top: 590px; text-align: center; font-size: 16.5px; line-height: 24px; }
  .process-copy { top: 676px; }
  .body-copy { font-size: 16.5px; line-height: 24.5px; text-align: justify; }
  sup { font-size: 10px; line-height: 0; }

  .adjustments { position: absolute; left: 135px; top: 828px; display: grid; grid-template-columns: 240px 1fr; }
  .adjustments-label { font-size: 23px; font-weight: 400; color: var(--purple-deep); line-height: 30px; }
  .adjustments-list { list-style: none; font-size: 16.5px; }
  .adjustments-list li { line-height: 30px; margin-bottom: 21px; }
</style>
</head>
<body>
<div class="page">
  <div class="header-accent" role="img" aria-label="Decorative purple wave accent"></div>

  <h1 class="block page-title">Our Development Procedure</h1>

  <h2 class="block section-title design-title">DESIGN</h2>
  <p class="block body-copy design-copy">Our dedicated team are happy to liaise with you to create a look. We offer advice on fabric, colour and style. We have a catalogue of designs and looks that may be used as a design starting point to help bring your vision to life. We also offer graphic design solutions to complete the look.</p>

  <h2 class="block section-title sampling-title">SAMPLING</h2>
  <p class="block body-copy sampling-copy">An original sample may be provided to us as a fit reference. We can also sample from photos as a base. Please note it is the customer’s responsibility to ensure the design does not infringe any copyright laws.</p>

  <p class="block timing">Sampling time: 3-5 WEEKS</p>

  <p class="block body-copy process-copy">It generally takes 2-3 weeks for the 1<sup>st</sup> sample to be produced. We allow an extra 2 weeks for resampling with minor changes. Upon receiving the sample we require the customer to fit the sample and notify us of any fit adjustments as well as any design adjustments. Should there be a Major Adjustment, then the sampling time is pushed back to 3-5 weeks as the process begins again.</p>

  <div class="adjustments">
    <h3 class="adjustments-label">Minor Adjustments:</h3>
    <ul class="adjustments-list">
      <li>Sleeve length</li>
      <li>Body length</li>
      <li>Inseam length</li>
      <li>Stitch colour</li>
    </ul>
  </div>

  <div class="footer-band" aria-hidden="true"></div>
</div>
</body>
</html>
```